Design a book cover to attract readers! cover art!

I am looking for a design of a book cover. The working title of the book is: The Sideline Launch: Growing a Venture Around Your Day Job Author R. K. Holloway .....while the book is about balancing work, life, and building a parttime startup, it is also about how to make sure you can give the "F You" to your boss. Following this book will help you get that confidence, freedom, and surety that you are ok if you ever choose to leave your job, and make your part time startup full time.As a result, I'm looking for something catchy, funny, and not 'bland' I'm ok with raunchy, and silly - the book iself is supposed to be a FUN way to learn this; not be the bland and normal 'self help' book.

Target Market(s)

young career (21-28) as well as college/pre college (18-25)

Colors

Designer to choose colors to be used in the design.

Requirements
Must have
• -a spot for the ISBN number (bottom right back of the book)
• -back cover & front cover and a half inch edge cover
• -bottom left will have my company logo (Marlow Group) which you can add into the mockup if you'd like
Nice to have
• something funny/catching
• book expected size 6" by 9"

```html
<!DOCTYPE html>
<html lang="en">
<head>
<meta charset="utf-8">
<title>The Sideline Launch – Book Cover Wrap</title>
<link href="https://fonts.googleapis.com/css2?family=Alfa+Slab+One&family=Barlow+Semi+Condensed:ital,wght@0,400;0,500;1,500&family=Barlow:wght@400;500&display=swap" rel="stylesheet">
<style>
  :root {
    --page-bg: #f1ece0;
    --cover-blue: #2f8fcf;
    --band-blue: #27699a;
    --ink-white: #ffffff;
    --ink-body: #e9f4fb;
    --photo-dark: #35383d;
    --photo-mid: #6b7077;
    --photo-light: #eef0f2;
    --figure-tone: #6d9cc2;
  }
  * { margin: 0; padding: 0; box-sizing: border-box; }
  html, body { width: 1200px; height: 730px; overflow: hidden; }
  body { background: var(--page-bg); position: relative; font-family: "Barlow", sans-serif; }

  .cover-wrap {
    position: absolute; left: 180px; top: 65px;
    width: 840px; height: 600px; display: flex;
    box-shadow: 0 6px 18px rgba(0,0,0,.15);
  }
  .back-cover, .front-cover { position: relative; width: 400px; height: 600px; background: var(--cover-blue); overflow: hidden; }
  .spine { position: relative; width: 40px; height: 600px; background: var(--cover-blue); border-left: 1px solid rgba(0,0,0,.12); border-right: 1px solid rgba(0,0,0,.12); }

  /* front */
  .front-top-band { position: absolute; left: 0; top: 0; width: 400px; height: 110px; }
  .front-subtitle {
    position: absolute; top: 28px; left: 0; width: 100%; text-align: center;
    font-family: "Barlow Semi Condensed", sans-serif; font-style: italic; font-weight: 500;
    font-size: 22px; line-height: 26px; color: var(--ink-white);
  }
  .front-title {
    position: absolute; top: 132px; left: 0; width: 100%; text-align: center;
    font-family: "Alfa Slab One", serif; font-weight: 400; font-size: 40px; line-height: 52px;
    color: var(--ink-white); letter-spacing: .5px;
  }
  .front-photo { position: absolute; left: 0; top: 300px; width: 400px; height: 220px; }
  .front-bottom-band {
    position: absolute; left: 0; bottom: 0; width: 400px; height: 80px;
    background: var(--band-blue); display: flex; justify-content: center; align-items: center;
  }
  .author-frame {
    position: relative; padding: 2px 12px 4px;
    border: 1.5px solid var(--ink-white); border-top: none;
    color: var(--ink-white); text-align: center;
    font-family: "Barlow Semi Condensed", sans-serif; font-weight: 500; font-size: 13px; line-height: 16px;
  }

  /* spine */
  .spine-title {
    position: absolute; top: 40px; left: 50%; transform: translateX(-50%);
    writing-mode: vertical-rl; font-family: "Alfa Slab One", serif; font-size: 18px;
    color: var(--ink-white); letter-spacing: .5px; white-space: nowrap;
  }
  .spine-author {
    position: absolute; bottom: 30px; left: 50%; transform: translateX(-50%);
    writing-mode: vertical-rl; font-family: "Barlow Semi Condensed", sans-serif; font-weight: 500;
    font-size: 11px; color: var(--ink-white); white-space: nowrap;
  }

  /* back */
  .back-blurb {
    position: absolute; top: 72px; left: 28px; width: 344px; text-align: center;
    font-size: 9.5px; line-height: 12.5px; color: var(--ink-body);
  }
  .back-blurb p + p { margin-top: 12px; }
  .back-illustration { position: absolute; left: 20px; top: 235px; width: 260px; height: 190px; }
  .back-bottom-band { position: absolute; left: 0; bottom: 0; width: 400px; height: 130px; }
  .back-tagline {
    position: absolute; left: 22px; top: 446px; width: 150px;
    font-size: 10px; line-height: 13px; color: var(--ink-body);
  }
  .logo-spot { position: absolute; left: 22px; top: 520px; width: 130px; height: 50px; background: var(--ink-white); border: 1px solid #c9d3da; }
  .isbn-spot { position: absolute; left: 208px; top: 432px; width: 112px; height: 140px; background: var(--ink-white); border: 1px solid #b9c4cc; border-radius: 10px; }
</style>
</head>
<body>
  <div class="cover-wrap">
    <section class="back-cover">
      <div class="back-blurb">
        <p>Your boss gets your best hours, but your evenings belong to you. This book shows how to turn spare nights and weekends into a real business without losing your paycheck, your sleep, or your sense of humor. Learn to test ideas fast, find first customers, protect your time, and build the quiet confidence that lets you walk out whenever you choose.</p>
        <p>Packed with plain steps, honest stories and a few jokes at the expense of middle management, it is the fun guide to going from side hustle to full time.</p>
      </div>
      <svg class="back-illustration" role="img" aria-label="Illustration of an office worker in shirt and tie balancing on a tightrope" viewBox="0 0 260 190">
        <defs>
          <radialGradient id="figureGlow" cx="50%" cy="45%" r="55%">
            <stop offset="0" stop-color="var(--figure-tone)"/>
            <stop offset="1" stop-color="var(--cover-blue)"/>
          </radialGradient>
        </defs>
        <rect width="260" height="190" fill="url(#figureGlow)"/>
      </svg>
      <svg class="back-bottom-band" viewBox="0 0 400 130" preserveAspectRatio="none" aria-hidden="true">
        <path d="M0 20 Q200 -8 400 14 L400 130 L0 130 Z" fill="var(--band-blue)"/>
      </svg>
      <p class="back-tagline">Keep your job, build your dream, and leave on your own terms.</p>
      <div class="logo-spot"></div>
      <div class="isbn-spot"></div>
    </section>

    <section class="spine">
      <span class="spine-title">THE SIDELINE LAUNCH</span>
      <span class="spine-author">R. K. Holloway</span>
    </section>

    <section class="front-cover">
      <svg class="front-top-band" viewBox="0 0 400 110" preserveAspectRatio="none" aria-hidden="true">
        <path d="M0 0 H400 V78 Q220 62 0 102 Z" fill="var(--band-blue)"/>
      </svg>
      <p class="front-subtitle">Growing a Venture Around<br>Your Day Job</p>
      <h1 class="front-title">THE<br>SIDELINE<br>LAUNCH</h1>
      <svg class="front-photo" role="img" aria-label="Photo of a blue wooden game pawn balanced between a white disc marked life and a dark disc marked work" viewBox="0 0 400 220" preserveAspectRatio="none">
        <defs>
          <linearGradient id="photoTone" x1="0" y1="0.3" x2="1" y2="0.7">
            <stop offset="0" stop-color="var(--photo-light)"/>
            <stop offset=".3" stop-color="var(--photo-mid)"/>
            <stop offset=".5" stop-color="var(--photo-dark)"/>
            <stop offset=".85" stop-color="var(--photo-dark)"/>
            <stop offset="1" stop-color="var(--cover-blue)"/>
          </linearGradient>
          <linearGradient id="photoFade" x1="0" y1="0" x2="0" y2="1">
            <stop offset="0" stop-color="var(--cover-blue)" stop-opacity="1"/>
            <stop offset=".3" stop-color="var(--cover-blue)" stop-opacity=".7"/>
            <stop offset=".6" stop-color="var(--cover-blue)" stop-opacity="0"/>
          </linearGradient>
        </defs>
        <rect width="400" height="220" fill="url(#photoTone)"/>
        <rect width="400" height="220" fill="url(#photoFade)"/>
      </svg>
      <div class="front-bottom-band">
        <div class="author-frame">Author:<br>R. K. Holloway</div>
      </div>
    </section>
  </div>
</body>
</html>
```